JMT - Business Card Design Project

We need a business card based on our logo
Updates

Hi I just upload logo file in AI format Thanks and regards

Target Market(s)

Bank, Big companies, Business owners

Industry/Entity Type

Business

Font styles to use
Sans Serif

```html
<!DOCTYPE html>
<html lang="fr">
<head>
<meta charset="utf-8">
<title>JMT – Carte de visite</title>
<link rel="stylesheet" href="https://fonts.googleapis.com/css2?family=Questrial&display=swap">
<style>
  :root {
    --backdrop: #1c1c1e;
    --card: #ffffff;
    --navy: #143463;
    --navy-dark: #0f2850;
    --slate: #8a9aa6;
    --ink-light: #d9e0ea;
    --brand: #1b3a6b;
  }
  * { margin: 0; padding: 0; box-sizing: border-box; }
  html, body {
    width: 1200px;
    height: 872px;
    overflow: hidden;
    background: var(--backdrop);
    font-family: "Questrial", "Century Gothic", sans-serif;
  }
  .business-card {
    position: absolute;
    left: 150px;
    top: 179px;
    width: 900px;
    height: 514px;
    background: var(--card);
    box-shadow: 0 20px 50px rgba(0,0,0,0.55);
  }
  .brand-block {
    position: absolute;
    left: 60px;
    top: 150px;
    width: 400px;
  }
  .brand-name {
    font-size: 150px;
    line-height: 0.9;
    color: var(--brand);
    letter-spacing: -2px;
  }
  .firm-name {
    margin-top: 8px;
    font-size: 25px;
    color: var(--brand);
    letter-spacing: 0.5px;
  }
  .firm-services {
    margin-top: 4px;
    font-size: 12px;
    color: var(--slate);
    letter-spacing: 0.8px;
    padding-left: 40px;
  }
  .contact-panel {
    position: absolute;
    left: 505px;
    top: 90px;
    right: 0;
    height: 320px;
    background: linear-gradient(135deg, var(--navy) 0%, var(--navy-dark) 100%);
    color: var(--ink-light);
  }
  .holder {
    position: absolute;
    right: 50px;
    top: 42px;
    text-align: right;
  }
  .holder-name { font-size: 36px; line-height: 1.1; }
  .holder-role { font-size: 30px; line-height: 1.15; }
  .contact-list {
    position: absolute;
    left: 70px;
    top: 170px;
    list-style: none;
  }
  .contact-item {
    display: flex;
    align-items: center;
    gap: 10px;
    font-size: 28px;
    line-height: 42px;
  }
  .contact-item svg {
    width: 22px;
    height: 22px;
    fill: var(--ink-light);
    stroke: var(--ink-light);
  }
</style>
</head>
<body>
  <div class="business-card">
    <div class="brand-block">
      <div class="brand-name">JMT</div>
      <div class="firm-name">Cabinet Marlot &amp; Associés</div>
      <div class="firm-services">Expertise-comptable - Audit - Conseil</div>
    </div>

    <div class="contact-panel">
      <div class="holder">
        <div class="holder-name">Name</div>
        <div class="holder-role">Designation</div>
      </div>
      <ul class="contact-list">
        <li class="contact-item">
          <svg viewBox="0 0 24 24" aria-hidden="true"><path stroke="none" d="M6.6 10.8a15.1 15.1 0 0 0 6.6 6.6l2.2-2.2a1 1 0 0 1 1-.25 11.4 11.4 0 0 0 3.6.57 1 1 0 0 1 1 1V20a1 1 0 0 1-1 1A17 17 0 0 1 3 4a1 1 0 0 1 1-1h3.5a1 1 0 0 1 1 1c0 1.25.2 2.45.57 3.57a1 1 0 0 1-.25 1z"/></svg>
          <span>Ph</span>
        </li>
        <li class="contact-item">
          <svg viewBox="0 0 24 24" aria-hidden="true"><path stroke="none" d="M2 5h20v14H2z"/><path fill="none" stroke="#143463" stroke-width="1.6" d="M2 5l10 8 10-8"/></svg>
          <span>Email</span>
        </li>
        <li class="contact-item">
          <svg viewBox="0 0 24 24" aria-hidden="true"><g fill="none" stroke-width="1.6"><circle cx="12" cy="12" r="9.5"/><ellipse cx="12" cy="12" rx="4" ry="9.5"/><path d="M2.5 12h19M4 7h16M4 17h16"/></g></svg>
          <span>Web</span>
        </li>
      </ul>
    </div>
  </div>
</body>
</html>
```